New website for Fribrix.se - self employment agency for freelance workers

[NOTE THE CODED ADD-ON HAS BEEN INCLUDED ALREADY (DC ADMIN)] New layout based on Wordpress themes including migration of existing content at fribrix.se. Want to use existing logotype as guideline for total layout concept. Please use existing structure and text content on fribrix.se. Existing pictures are optional to reuse. The secured part of the existing website under "Logga in" is not part of this project.

Target Market(s)

Self employment within all industries and ages above 16.

Industry/Entity Type

Finance And Accounting

Font styles to use
Other font styles liked:
• Should match with logotype

Colors
3176b5
85abd2
cfdeed

Requirements
Must have
• Ready to use wordpress themes. Include salary calculation bar as in existing website. Multi lingual ready(today only in Swedish). Mobile client responsive.

```html
<!DOCTYPE html>
<html lang="sv">
<head>
<meta charset="utf-8">
<title>Fribrix – Egenanställning</title>
<link rel="stylesheet" href="https://fonts.googleapis.com/css2?family=Open+Sans:wght@400;600;700;800&display=swap">
<style>
  :root {
    --blue-primary: #3176b5;
    --blue-mid: #85abd2;
    --blue-pale: #cfdeed;
    --blue-bright: #1ea3e3;
    --blue-button: #0b62d6;
    --blue-soft: #5b9bd8;
    --ink: #2b2b2b;
    --ink-body: #4a4a4a;
    --frame: #e6e6e6;
    --page: #ffffff;
    --band: #f2f2f2;
    --field-border: #c9c9c9;
  }
  * { box-sizing: border-box; margin: 0; padding: 0; }
  html, body { width: 784px; height: 1200px; overflow: hidden; }
  body {
    background: var(--frame);
    font-family: "Open Sans", Arial, sans-serif;
    color: var(--ink);
    position: relative;
  }
  .page {
    position: absolute; left: 10px; top: 10px; width: 764px; height: 1180px;
    background: var(--page);
  }
  /* header */
  .brand {
    position: absolute; left: 14px; top: 20px; width: 150px; height: 82px; z-index: 3;
    background: var(--page);
    display: flex; flex-direction: column; align-items: center; justify-content: center; gap: 6px;
  }
  .brand-mark { width: 30px; height: 30px; background: var(--blue-primary); }
  .brand-name { font-size: 22px; line-height: 26px; font-weight: 400; letter-spacing: 2px; color: var(--ink); }
  .info-bar {
    position: absolute; right: 16px; top: 0; width: 322px; height: 24px;
    background: var(--blue-bright);
    clip-path: polygon(0 0, 100% 0, 100% 100%, 18px 100%);
    display: flex; align-items: center; gap: 6px; padding-left: 36px;
    color: #fff; font-size: 9.5px; font-weight: 700;
  }
  .info-bar svg { width: 13px; height: 13px; }
  .social { display: flex; gap: 3px; margin-left: 14px; }
  .social span { width: 13px; height: 13px; border: 1.4px solid #fff; border-radius: 50%; }
  .main-nav {
    position: absolute; right: 40px; top: 55px; display: flex; align-items: center; gap: 13px;
    font-size: 10px; font-weight: 700; color: var(--ink);
  }
  .main-nav .current { color: var(--blue-primary); border-bottom: 2px solid var(--blue-primary); padding-bottom: 2px; }
  .main-nav .login { background: var(--blue-bright); color: #fff; padding: 5px 7px; border-radius: 2px; }
  /* hero */
  .hero {
    position: absolute; left: 0; top: 84px; width: 764px; height: 362px; z-index: 1;
    box-shadow: 0 10px 12px -8px rgba(0,0,0,.35);
  }
  .hero-left {
    position: absolute; left: 0; top: 0; width: 384px; height: 100%;
    background: linear-gradient(180deg, #dfe8ef 0%, #c9d6e0 40%, #8f9a8a 62%, #a88f5e 78%, #8d7448 100%);
  }
  .hero-right {
    position: absolute; left: 384px; top: 0; width: 380px; height: 100%;
    background: linear-gradient(120deg, #7a5230 0%, #a07248 40%, #b48a60 60%, #d8d3cc 85%, #c8c4bf 100%);
  }
  .hero-title {
    position: absolute; left: 176px; top: 144px; width: 414px; height: 96px;
    background: rgba(255,255,255,.35);
    border: 3px solid #fff; outline: 2px solid rgba(255,255,255,.5); outline-offset: 3px;
    display: flex; align-items: center; justify-content: center;
    font-size: 43px; font-weight: 700; color: #fff; text-shadow: 0 2px 4px rgba(0,0,0,.35);
  }
  .hero-cta {
    position: absolute; left: 276px; top: 278px; width: 216px; height: 36px;
    background: var(--blue-button); border-radius: 18px;
    color: #fff; font-family: Arial, "Open Sans", sans-serif; font-weight: 700; font-size: 19px;
    display: flex; align-items: center; justify-content: center;
  }
  /* intro */
  .intro-heading {
    position: absolute; left: 0; top: 482px; width: 764px; text-align: center;
    font-size: 17px; font-weight: 700; color: var(--blue-bright);
  }
  .intro-text {
    position: absolute; left: 40px; top: 536px; width: 720px;
    font-size: 8.7px; line-height: 13.3px; color: var(--ink-body); white-space: nowrap;
  }
  .intro-text p + p { margin-top: 13.3px; }
  /* contact */
  .contact {
    position: absolute; left: 0; top: 724px; width: 764px; height: 310px; background: var(--band);
  }
  .contact-heading {
    position: absolute; left: 0; top: 38px; width: 764px;
    display: flex; align-items: center; justify-content: center; gap: 12px;
    font-size: 17px; font-weight: 700;
  }
  .contact-heading::before, .contact-heading::after {
    content: ""; width: 66px; height: 1px; background: #cfcfcf;
  }
  .contact-heading .accent { color: var(--blue-soft); }
  .field {
    position: absolute; height: 30px; background: #fff; border: 1.5px solid var(--field-border);
    border-radius: 3px; padding: 7px 10px; font-size: 10.5px; font-weight: 600; color: var(--ink);
  }
  .field.name { left: 64px; top: 86px; width: 207px; }
  .field.email { left: 279px; top: 86px; width: 205px; }
  .field.subject { left: 493px; top: 86px; width: 205px; }
  .field.message { left: 64px; top: 125px; width: 634px; height: 88px; }
  .send {
    position: absolute; left: 320px; top: 221px; width: 124px; height: 28px;
    background: var(--blue-bright); border-radius: 4px; box-shadow: 0 2px 3px rgba(0,0,0,.25);
    color: #fff; font-size: 9.5px; font-weight: 700;
    display: flex; align-items: center; justify-content: center;
  }
  /* footer */
  .footer-brand {
    position: absolute; left: 0; top: 1058px; width: 764px;
    display: flex; flex-direction: column; align-items: center; gap: 8px;
  }
  .footer-brand .brand-mark { width: 36px; height: 36px; }
  .footer-brand .brand-name { font-size: 24px; line-height: 28px; }
  .footer-rule { position: absolute; left: 0; top: 1150px; width: 764px; height: 1px; background: #9bb3c7; }
  .copyright {
    position: absolute; left: 0; top: 1162px; width: 764px; text-align: center;
    font-size: 8px; font-weight: 700; color: var(--ink);
  }
</style>
</head>
<body>
<div class="page">
  <header>
    <div class="brand">
      <span class="brand-mark"></span>
      <span class="brand-name">FRIBRIX</span>
    </div>
    <div class="info-bar">
      <svg viewBox="0 0 16 16" aria-hidden="true"><circle cx="8" cy="8" r="7" fill="none" stroke="#fff" stroke-width="1.4"/><path d="M5.3 4.5l1.4-.3.7 1.8-.9.7a5 5 0 0 0 2.8 2.8l.7-.9 1.8.7-.3 1.4c-3.6.3-6.5-2.6-6.2-6.2z" fill="#fff"/></svg>
      <span>FOR INFORMATION : 08-555 0142</span>
      <span class="social"><span></span><span></span><span></span></span>
    </div>
    <nav class="main-nav">
      <span class="current">Hem</span>
      <span>Jobba som egenanställd</span>
      <span>Företag</span>
      <span>Om oss</span>
      <span class="login">Logga in</span>
    </nav>
  </header>

  <section class="hero">
    <div class="hero-left" role="img" aria-label="Photo of a person with raised arms on a grassy mountain top above misty valleys"></div>
    <div class="hero-right" role="img" aria-label="Photo of a hand writing in a notebook on a wooden desk beside a cup of coffee"></div>
    <div class="hero-title">You can do it solo</div>
    <div class="hero-cta">Bli soloföretagare</div>
  </section>

  <h1 class="intro-heading">Fakturera utan eget företag, anlita medarbetare utan att anställa</h1>
  <div class="intro-text">
    <p>Fokusera på att utföra uppdraget så tar vi hand om resten<br>
    Fribrix är ett egenanställningsföretag som förenklar, effektiviserar och tryggar administrationen och hjälper dig som egen att fakturera utan att behöva ett eget företag.<br>
    Slipp administrationen och fokusera på det du gör bäst. Läs mer...</p>
    <p>Vi hanterar fakturering, skatter, avgifter och moms åt dig som egenanställd<br>
    Vi erbjuder ett heltäckande försäkringsskydd<br>
    Vi sköter utbetalning av din lön och bevakning av dina kundfakturor så att du får betalt<br>
    Få möjlighet till expressbetalning inom 24 timmar</p>
    <p>Välj ut och anlita dina kompetenta medarbetare utan att anställa<br>
    För företag och privatpersoner erbjuder Fribrix möjligheten att anlita medarbetare utan att behöva anställa. Du väljer medarbetare och Fribrix tar hela arbetsgivaransvaret.<br>
    Vi förenklar och effektiviserar din hantering av externa medarbetare. Läs mer...</p>
  </div>

  <section class="contact">
    <h2 class="contact-heading"><span>Contact us! <span class="accent">Complete the form below to get started...</span></span></h2>
    <div class="field name">Your Name</div>
    <div class="field email">Your Email</div>
    <div class="field subject">Your Subject</div>
    <div class="field message">Message</div>
    <div class="send">SEND YOUR MESSAGE</div>
  </section>

  <footer>
    <div class="footer-brand">
      <span class="brand-mark"></span>
      <span class="brand-name">FRIBRIX</span>
    </div>
    <div class="footer-rule"></div>
    <p class="copyright">© 2018 FRIBRIX I ALL RIGHTS RESERVED</p>
  </footer>
</div>
</body>
</html>
```